Copperleaf Motorized Shade Business Card

Hello, we've had our logo made. Now we are looking for a clean and cool looking business card. One side can just be the logo with any design elements that might look good with it. The other side will be Name, Phone Number and Email. There will not be an address on the card.

```html
<!DOCTYPE html>
<html lang="en">
<head>
<meta charset="utf-8">
<title>Copperleaf Motorized Shade Business Card</title>
<link rel="stylesheet" href="https://fonts.googleapis.com/css2?family=Source+Sans+3:wght@400;600;700;800&display=swap">
<style>
  :root {
    --stage: #b3b3b3;
    --navy: #0b3a73;
    --sky: #2aa6df;
    --sun: #f2b705;
    --paper: #ffffff;
    --rule: #c9ced6;
  }
  html, body { margin: 0; padding: 0; overflow: hidden; }
  body {
    width: 1200px; height: 800px;
    background: var(--stage);
    position: relative;
    font-family: "Source Sans 3", sans-serif;
  }
  .card {
    position: absolute; top: 262px;
    width: 478px; height: 274px;
    overflow: hidden;
  }
  .card-front { left: 104px; background: var(--paper); }
  .card-back { left: 620px; background: var(--navy); }

  .brand { position: absolute; display: flex; align-items: center; gap: 6px; font-weight: 800; letter-spacing: 0.02em; }
  .brand-mark { display: block; }
  .brand-small { right: 36px; top: 124px; color: var(--navy); font-size: 15px; }
  .brand-small .brand-mark { width: 10px; height: 10px; background: var(--sky); }
  .brand-large { left: 0; right: 0; top: 114px; justify-content: center; color: var(--paper); font-size: 40px; gap: 14px; }
  .brand-large .brand-mark { width: 30px; height: 30px; background: var(--paper); }

  .person { position: absolute; left: 32px; top: 122px; }
  .person-name { margin: 0; color: var(--navy); font-size: 23px; font-weight: 700; line-height: 1; }
  .person-title { margin: 5px 0 0; color: var(--sun); font-size: 7px; font-weight: 700; letter-spacing: 0.12em; }
  .divider { position: absolute; left: 32px; right: 36px; top: 172px; height: 1px; background: var(--rule); }

  .contact { position: absolute; left: 32px; top: 186px; margin: 0; padding: 0; list-style: none; }
  .contact li { display: flex; align-items: center; gap: 8px; height: 19px; color: var(--sky); font-size: 10px; font-weight: 600; }
  .contact svg { width: 10px; height: 10px; fill: var(--sun); }

  .band { position: absolute; left: 0; bottom: 0; width: 478px; height: 28px; }
  .website { position: absolute; right: 36px; bottom: 7px; color: var(--sky); font-size: 10px; font-weight: 600; line-height: 1; }
</style>
</head>
<body>
  <section class="card card-front" aria-label="Card front">
    <div class="brand brand-small"><span class="brand-mark"></span>COPPERLEAF</div>

    <div class="person">
      <h1 class="person-name">Dara Quinlan</h1>
      <p class="person-title">PRESIDENT</p>
    </div>
    <div class="divider"></div>

    <ul class="contact">
      <li><svg viewBox="0 0 10 10" aria-hidden="true"><path d="M2 0h2l1 3-1.5 1a6 6 0 0 0 2.5 2.5L7 5l3 1v2c0 1-1 2-2 2A8 8 0 0 1 0 2c0-1 1-2 2-2z"/></svg>555.014.2288</li>
      <li><svg viewBox="0 0 10 10" aria-hidden="true"><path d="M2.5 0h5a1 1 0 0 1 1 1v8a1 1 0 0 1-1 1h-5a1 1 0 0 1-1-1V1a1 1 0 0 1 1-1zm0 1.5v6h5v-6z"/></svg>555.017.3416</li>
      <li><svg viewBox="0 0 10 10" aria-hidden="true"><path d="M0 2h10v6H0zM1 2.8v.6l4 2.4 4-2.4v-.6L5 5.2z"/></svg>hello@copperleaf.example</li>
    </ul>

    <svg class="band" viewBox="0 0 478 28" aria-hidden="true">
      <path d="M0 16H140C158 16 164 2 190 2H478V28H0Z" fill="var(--navy)"/>
    </svg>
    <div class="website">www.copperleaf.example</div>
  </section>

  <section class="card card-back" aria-label="Card back">
    <div class="brand brand-large"><span class="brand-mark"></span>COPPERLEAF</div>
  </section>
</body>
</html>
```